Cobalt Margin Funds Bus card and Logo

I need a logo design and Bus card design. The fund focuses on evaluating and investing in minerals (sub-surface rights) and real estate.

Cobalt margin refers to a book of knowledge that each plebe gets when entering the Harwick Civic Academy (my alma mater)

Target Market(s)

Investors and financial advisors

Contact Information for Business Card

Simple - perhaps a logo with a theme on book of knowledge

Logo Text

Ex Scientia Imperium

Font styles to use
Serif
Sans Serif

Colors

Designer to choose colors to be used in the design.

Requirements
Must have
• memorable logo that is relatively simple

```html
<!DOCTYPE html>
<html lang="en">
<head>
<meta charset="utf-8">
<title>Cobalt Margin Funds – Business Card</title>
<link rel="stylesheet" href="https://fonts.googleapis.com/css2?family=Lato:wght@400;700&family=Roboto:wght@500&display=swap">
<style>
  :root {
    --backdrop: #d9d9d9;
    --card-blue: #3399cf;
    --card-green: #8cc63f;
    --paper: #ffffff;
    --ink-dark: #222222;
    --ink-light: #ffffff;
  }
  html, body {
    margin: 0;
    padding: 0;
    width: 1200px;
    height: 802px;
    overflow: hidden;
    background: var(--backdrop);
  }
  .canvas {
    position: relative;
    width: 1200px;
    height: 802px;
  }
  .card {
    position: absolute;
    top: 274px;
    width: 442px;
    height: 265px;
    overflow: hidden;
    box-shadow: 0 2px 6px rgba(0,0,0,0.25);
  }
  .card--front {
    left: 136px;
    background: var(--card-blue);
    font-family: "Lato", sans-serif;
    color: var(--ink-light);
  }
  .card--back {
    left: 624px;
    background: var(--paper);
  }
  .front-shapes {
    position: absolute;
    left: 0;
    top: 0;
    width: 442px;
    height: 265px;
  }
  .front-shapes .accent-curve { fill: var(--card-green); }
  .front-shapes .brand-disc { fill: var(--paper); }
  .front-brand {
    position: absolute;
    left: 118px;
    top: 150px;
    width: 150px;
    margin: 0;
    font-family: "Lato", sans-serif;
    font-weight: 700;
    font-size: 18px;
    line-height: 1.2;
    text-align: center;
    color: var(--card-blue);
  }
  .holder {
    position: absolute;
    right: 21px;
    top: 29px;
    text-align: right;
  }
  .holder__name {
    margin: 0;
    font-weight: 700;
    font-size: 17.5px;
    letter-spacing: 0.2px;
    line-height: 1.1;
  }
  .holder__role {
    margin: 0;
    font-size: 13px;
    line-height: 1.15;
  }
  .address {
    position: absolute;
    right: 24px;
    top: 111px;
    margin: 0;
    font-style: normal;
    font-size: 13px;
    line-height: 15.8px;
    text-align: right;
  }
  .contacts {
    position: absolute;
    right: 24px;
    top: 176px;
    margin: 0;
    padding: 0;
    list-style: none;
    font-size: 13px;
    line-height: 15.8px;
    text-align: right;
  }
  .contacts li {
    display: flex;
    justify-content: flex-end;
    align-items: center;
    gap: 3px;
  }
  .contacts svg {
    width: 9px;
    height: 9px;
    fill: var(--ink-light);
  }
  .back-brand {
    position: absolute;
    left: 0;
    right: 0;
    top: 58px;
    display: flex;
    flex-direction: column;
    align-items: center;
  }
  .back-brand__dot {
    width: 58px;
    height: 58px;
    margin-left: -10px;
    border-radius: 50%;
    background: var(--card-blue);
  }
  .back-brand__name {
    margin: 14px 0 0;
    font-family: "Roboto", sans-serif;
    font-weight: 500;
    font-size: 30px;
    line-height: 1;
    letter-spacing: 0.2px;
    text-align: center;
    color: var(--ink-dark);
  }
  .back-brand__name span {
    display: block;
    margin-top: 8px;
    font-size: 11.5px;
    letter-spacing: 10px;
    padding-left: 10px;
  }
</style>
</head>
<body>
<main class="canvas">
  <section class="card card--front" aria-label="Business card front">
    <svg class="front-shapes" viewBox="0 0 442 265" aria-hidden="true">
      <path class="accent-curve" d="M0 0 H134 C112 70 100 160 116 265 H0 Z"/>
      <circle class="brand-disc" cx="192" cy="172" r="86"/>
    </svg>
    <p class="front-brand">Cobalt Margin<br>Funds</p>
    <div class="holder">
      <h1 class="holder__name">DARREN KOWAL</h1>
      <p class="holder__role">Managing Director</p>
    </div>
    <address class="address">
      12345, Address<br>
      Goes Here<br>
      Country Name, 123456
    </address>
    <ul class="contacts">
      <li>044-123 456 789
        <svg viewBox="0 0 10 10" aria-hidden="true"><path d="M1 3 Q5 0 9 3 L8 4.5 L6.5 4 L6.5 3 Q5 2.5 3.5 3 L3.5 4 L2 4.5 Z M2.5 5 H7.5 L8.5 9 H1.5 Z"/></svg>
      </li>
      <li>044-123 456 789
        <svg viewBox="0 0 10 10" aria-hidden="true"><path d="M3 0.5 H7 V9.5 H3 Z M3.8 1.5 V7.5 H6.2 V1.5 Z" fill-rule="evenodd"/></svg>
      </li>
      <li>info@webname.com
        <svg viewBox="0 0 10 10" aria-hidden="true"><path d="M0.5 2 H9.5 V8 H0.5 Z M1.3 2.6 L5 5.5 L8.7 2.6 Z" fill-rule="evenodd"/></svg>
      </li>
      <li>www.websitename.com
        <svg viewBox="0 0 10 10" aria-hidden="true"><circle cx="5" cy="5" r="4.5"/></svg>
      </li>
    </ul>
  </section>

  <section class="card card--back" aria-label="Business card back">
    <div class="back-brand">
      <span class="back-brand__dot"></span>
      <h2 class="back-brand__name">COBALT MARGIN<span>FUNDS</span></h2>
    </div>
  </section>
</main>
</body>
</html>
```